Web Page for marketing online agency

We are an online marketing agency that is acing the direct response model. We engage with our customers throughout different marketing techniques as research copy-writing, advertisements and content writing. We would need a website design that will have four main aspects: The Vision; stating who we are, The Mission; stating what we do, The Team And It's Values, and a Contact Form. For this design we would want a sharp, clean and smart approach, with illustrated elements or suggestive images. You can use the attached copy, the logo, the USP and the motto. Please integrate them as you see fit while keeping in mind the previous needs and copy. This website is going to be our connection with our possible partners, future colleagues and even our clients. You may submit a design for one page or integrate the 4 different aspects on separate web pages.
Target Market(s)
business partners, future employees, age range 25-60
Industry/Entity Type
Direct Marketing
Number of Pages Required
1 page
Requirements
Must have
- Menu / Header
- 4 Parts or 4 Pages including: vision, mission, team, contact
- Logo
- Motto: Direct Brilliance
- USP: We help people help themselves.
- The copy attached
Nice to have
- Representative illustrated images or elements
Should not have
- A boring design, classical design - Pagequill like

```html
<!DOCTYPE html>
<html lang="en">
<head>
<meta charset="utf-8">
<title>NovaKin</title>
<link href="https://fonts.googleapis.com/css2?family=Quicksand:wght@400;500;600;700&family=Nunito:wght@700;800&display=swap" rel="stylesheet">
<style>
:root{
  --blue:#35aee2;
  --ink:#333;
  --muted:#777;
  --soft:#f0f0f0;
  --white:#fff;
  --black:#000;
  --bar:#333;
  --fb:#3b5998;
  --red:#d8432f;
  --sky:#32aee6;
}
*{box-sizing:border-box;margin:0;padding:0}
html,body{width:1200px;height:2635px;overflow:hidden}
body{position:relative;background:var(--white);font-family:"Quicksand",sans-serif;color:var(--ink)}

/* header */
.site-header{position:absolute;left:0;top:0;width:1200px;height:125px;background:var(--white);box-shadow:0 2px 6px rgba(0,0,0,.08);z-index:2}
.brand{position:absolute;left:78px;top:46px;display:flex;align-items:center;gap:12px;font:700 40px/1 "Quicksand",sans-serif;color:var(--ink)}
.brand-dot{width:22px;height:22px;border-radius:50%;background:var(--blue)}
.main-nav{position:absolute;top:56px;left:0;width:1200px;font-size:18px;font-weight:500;color:#555}
.main-nav span{position:absolute}
.search-btn{position:absolute;left:882px;top:46px;width:42px;height:42px;border:2px solid var(--blue);border-radius:50%}
.phone-pill{position:absolute;left:945px;top:46px;width:178px;height:42px;border-radius:21px;background:var(--blue);color:var(--white);font-size:17px;font-weight:600;display:flex;align-items:center;justify-content:center;gap:8px;white-space:nowrap}

/* hero */
.hero-photo{position:absolute;left:0;top:125px;width:1200px;height:573px;background:linear-gradient(100deg,#2d3f5c 0%,#8a97a8 30%,#c9d6e0 55%,#e6eef3 80%,#b9c6cf 100%)}
.hero-panel{position:absolute;left:706px;top:228px;width:415px;height:313px;background:rgba(53,174,226,.9);border-radius:12px;color:var(--white);text-align:center}
.hero-panel h1{margin-top:28px;font:800 43px/46px "Nunito",sans-serif}
.hero-panel p{margin-top:20px;font-size:16px;line-height:27px}
.btn-light{position:absolute;left:99px;top:217px;width:218px;height:61px;background:var(--white);color:var(--blue);font-size:21px;font-weight:500;display:flex;align-items:center;justify-content:center}

/* values */
.values-band{position:absolute;left:0;top:698px;width:1200px;height:216px;background:var(--white);border-bottom:2px solid #ddd}
.notch{position:absolute;left:590px;top:904px;width:20px;height:20px;background:var(--white);border-right:2px solid #ddd;border-bottom:2px solid #ddd;transform:rotate(45deg)}
.value{position:absolute;top:655px;width:148px;text-align:center}
.value-frame{width:148px;height:141px;background:var(--white);padding:9px;box-shadow:0 1px 4px rgba(0,0,0,.12)}
.value-icon{width:130px;height:123px;background:var(--blue);display:flex;align-items:center;justify-content:center}
.value-label{margin-top:20px;font-size:21px;line-height:24px;color:var(--ink)}

/* who */
.section-title{font-size:38px;font-weight:500;color:var(--ink);text-align:center}
.section-title b{color:var(--blue);font-weight:700}
.who-title{position:absolute;left:0;top:982px;width:1200px}
.who-lead{position:absolute;left:150px;top:1046px;width:900px;text-align:center;font-size:18px;font-weight:700;line-height:26px;color:#444}
.who-body{position:absolute;left:100px;top:1112px;width:1000px;text-align:center;font-size:14px;line-height:26px;color:var(--muted)}
.btn-blue{position:absolute;left:517px;top:1188px;width:166px;height:61px;background:var(--blue);color:var(--white);font-size:21px;font-weight:500;display:flex;align-items:center;justify-content:center}

/* do */
.do-photo{position:absolute;left:0;top:1323px;width:600px;height:467px;background:linear-gradient(135deg,#d9d5cf,#a0785a 45%,#8a6a52 60%,#cfccc7)}
.do-panel{position:absolute;left:600px;top:1323px;width:600px;height:467px;background:var(--soft)}
.do-title{position:absolute;left:664px;top:1380px;font-size:37px;font-weight:500;white-space:nowrap}
.do-title b{color:var(--blue);font-weight:700}
.do-sub{position:absolute;left:664px;top:1448px;width:500px;font-size:22px;line-height:32px;font-weight:500;white-space:nowrap}
.checks{position:absolute;left:664px;top:1519px;width:480px;list-style:none}
.checks li{position:relative;padding-left:34px;font-size:15px;line-height:24px;color:#555;margin-bottom:18px}
.checks li b{color:var(--blue);font-weight:700}
.checks svg{position:absolute;left:0;top:2px}
.do-close{position:absolute;left:664px;top:1672px;width:520px;font-size:22px;line-height:32px;font-weight:500;white-space:nowrap}

/* team values */
.team-band{position:absolute;left:0;top:1790px;width:1200px;height:491px;background:var(--blue);color:var(--white)}
.team-title{position:absolute;left:0;top:56px;width:1200px;text-align:center;font-size:38px;font-weight:500}
.team-title b{font-weight:700}
.trait{position:absolute;left:79px;display:flex;align-items:baseline;gap:12px}
.trait strong{font-size:23px;font-weight:700;white-space:nowrap}
.trait span{font-size:17px;line-height:25px;font-weight:500}
.member-card{position:absolute;left:822px;top:139px;width:194px;height:194px;background:var(--white);border-radius:8px;padding:10px}
.member-photo{width:174px;height:174px;border-radius:6px;background:linear-gradient(160deg,#5a4632,#2e241d 60%,#d8cfc4)}
.dots{position:absolute;left:901px;top:359px;display:flex;gap:3px}
.dots i{width:17px;height:17px;border:2px solid var(--white)}
.dots i:first-child{background:var(--white)}

/* footer */
.site-footer{position:absolute;left:0;top:2281px;width:1200px;height:281px;background:var(--black);color:var(--white)}
.foot-brand{position:absolute;left:0;top:88px;width:1200px;display:flex;justify-content:center;align-items:center;gap:10px;font:700 38px/1 "Quicksand",sans-serif}
.round-ico{position:absolute;width:40px;height:40px;border-radius:50%;background:var(--blue);display:flex;align-items:center;justify-content:center}
.foot-addr{position:absolute;left:134px;top:124px;font-size:15px;line-height:25px}
.foot-addr strong{display:block;font-size:16px;margin-bottom:4px}
.foot-nav{position:absolute;left:0;top:150px;width:1200px;text-align:center;font-size:15px}
.foot-nav .on{color:var(--blue)}
.foot-nav em{font-style:normal;margin:0 10px}
.social{position:absolute;top:195px;width:30px;height:30px;border-radius:50%}
.foot-contact{position:absolute;left:944px;font-size:15px}
.bottom-bar{position:absolute;left:0;top:2562px;width:1200px;height:73px;background:var(--bar);color:#ddd;font-size:14px}
.bottom-bar span{position:absolute;top:28px}
</style>
</head>
<body>

<header class="site-header">
  <div class="brand"><span>NovaKin</span><span class="brand-dot"></span></div>
  <nav class="main-nav">
    <span style="left:363px">Home</span>
    <span style="left:443px">About</span>
    <span style="left:527px">Vission</span>
    <span style="left:615px">Mission</span>
    <span style="left:708px">Team</span>
    <span style="left:789px">Contact</span>
  </nav>
  <div class="search-btn">
    <svg width="38" height="38" viewBox="0 0 38 38"><circle cx="17" cy="17" r="7" fill="none" stroke="#35aee2" stroke-width="2"/><line x1="22" y1="22" x2="27" y2="27" stroke="#35aee2" stroke-width="2.5"/></svg>
  </div>
  <div class="phone-pill">
    <svg width="18" height="18" viewBox="0 0 24 24"><path fill="#fff" d="M6.6 10.8a15 15 0 0 0 6.6 6.6l2.2-2.2a1 1 0 0 1 1-.25 11.4 11.4 0 0 0 3.6.6 1 1 0 0 1 1 1V20a1 1 0 0 1-1 1A17 17 0 0 1 3 4a1 1 0 0 1 1-1h3.5a1 1 0 0 1 1 1c0 1.25.2 2.45.6 3.6a1 1 0 0 1-.25 1z"/></svg>
    +1 555 010 4477
  </div>
</header>

<div class="hero-photo" role="img" aria-label="Photo of a team discussing work around a desk in a bright office"></div>
<div class="hero-panel">
  <h1>We help people<br>help themselves</h1>
  <p>We are specialized in the self-reliance market<br>and we serve conservative Americans</p>
  <div class="btn-light">GET STARTED NOW</div>
</div>

<div class="values-band"></div>
<div class="notch"></div>

<div class="value" style="left:172px">
  <div class="value-frame"><div class="value-icon">
    <svg width="70" height="70" viewBox="0 0 64 64" fill="none" stroke="#fff" stroke-width="3"><line x1="32" y1="8" x2="32" y2="54"/><line x1="12" y1="16" x2="52" y2="16"/><line x1="20" y1="56" x2="44" y2="56"/><path d="M6 36l6-20 6 20z"/><path d="M46 36l6-20 6 20z"/></svg>
  </div></div>
  <div class="value-label">Fairness</div>
</div>
<div class="value" style="left:350px">
  <div class="value-frame"><div class="value-icon">
    <svg width="70" height="70" viewBox="0 0 64 64" fill="#fff"><circle cx="24" cy="18" r="5"/><circle cx="40" cy="18" r="5"/><rect x="19" y="25" width="10" height="18" rx="3"/><rect x="35" y="25" width="10" height="18" rx="3"/><path d="M6 44q26 18 52 0" fill="none" stroke="#fff" stroke-width="3"/></svg>
  </div></div>
  <div class="value-label">Caring</div>
</div>
<div class="value" style="left:526px">
  <div class="value-frame"><div class="value-icon">
    <svg width="70" height="70" viewBox="0 0 64 64"><path fill="#fff" d="M32 6l22 8v14c0 14-10 24-22 30C20 52 10 42 10 28V14z"/><path d="M22 32l7 7 13-14" fill="none" stroke="#35aee2" stroke-width="4"/></svg>
  </div></div>
  <div class="value-label">Safety</div>
</div>
<div class="value" style="left:713px">
  <div class="value-frame"><div class="value-icon">
    <svg width="70" height="70" viewBox="0 0 64 64" fill="#fff"><circle cx="32" cy="14" r="6"/><rect x="25" y="22" width="14" height="20" rx="4"/><rect x="25" y="40" width="5" height="18"/><rect x="34" y="40" width="5" height="18"/><circle cx="14" cy="22" r="4"/><circle cx="50" cy="22" r="4"/></svg>
  </div></div>
  <div class="value-label">Freedom</div>
</div>
<div class="value" style="left:891px">
  <div class="value-frame"><div class="value-icon">
    <svg width="76" height="70" viewBox="0 0 70 64" fill="none" stroke="#fff" stroke-width="3" stroke-linejoin="round"><path d="M4 24l12-8 8 4"/><path d="M66 24l-12-8-12 4-10 8 4 4 10-6"/><path d="M16 36l10 10 6 4 8-2 12-12"/><path d="M4 24l12 12M66 24L54 36"/></svg>
  </div></div>
  <div class="value-label">Unconditioned<br>help</div>
</div>

<h2 class="section-title who-title">Who <b>We are?</b></h2>
<p class="who-lead">We are a direct response company that creates and sells information products and<br>services that millions of people find interesting and important in their lives.</p>
<p class="who-body">We are specialized in the self-reliance market and we serve conservative Americans.We are in this business to serve globally and to<br>grow individually.What we serve and inspire are people who need safety, comfort and peace of mind.</p>
<div class="btn-blue">READ MORE</div>

<div class="do-photo" role="img" aria-label="Top-down photo of a team working with laptops and papers at a wooden table"></div>
<div class="do-panel"></div>
<h2 class="do-title">What is it <b>that we do?</b></h2>
<p class="do-sub">We live and breathe direct response<br>marketing</p>
<ul class="checks">
  <li><svg width="20" height="20" viewBox="0 0 20 20"><rect x="1" y="3" width="15" height="15" fill="none" stroke="#35aee2" stroke-width="2"/><path d="M5 10l4 4 9-11" fill="none" stroke="#35aee2" stroke-width="2.5"/></svg>We create and aggregate great <b>information products.</b></li>
  <li><svg width="20" height="20" viewBox="0 0 20 20"><rect x="1" y="3" width="15" height="15" fill="none" stroke="#35aee2" stroke-width="2"/><path d="M5 10l4 4 9-11" fill="none" stroke="#35aee2" stroke-width="2.5"/></svg>We write content that <b>compels people to act.</b></li>
  <li><svg width="20" height="20" viewBox="0 0 20 20"><rect x="1" y="3" width="15" height="15" fill="none" stroke="#35aee2" stroke-width="2"/><path d="M5 10l4 4 9-11" fill="none" stroke="#35aee2" stroke-width="2.5"/></svg>We do <b>deep research</b> to offer simple quick and easy<br>solutions to people's most serious problems.</li>
</ul>
<p class="do-close">We create content and build solutions to<br>profound challenges for millions of people.</p>

<section class="team-band">
  <h2 class="team-title">What is it <b>that we do?</b></h2>
  <div class="trait" style="top:137px"><strong>Impact</strong><span>- leverage, maximum results, 80/20, greatness</span></div>
  <div class="trait" style="top:178px"><strong>Wisdom</strong><span>- learning mode “on”, practice of self-improvement as a lifestyle</span></div>
  <div class="trait" style="top:220px"><strong>Team spirit</strong><span>- cooperation and complementarity, synergy, yin &amp; yang</span></div>
  <div class="trait" style="top:261px"><strong>Courage</strong><span>- feel the fear and do it anyway</span></div>
  <div class="trait" style="top:302px"><strong>Innovation mindset</strong><span>- you recombine and reconnect things, so you can<br>solve old problems in new, better ways</span></div>
  <div class="trait" style="top:375px"><strong>Ownership</strong><span>“leaders must own everything in their world. There is no one<br>else to blame.”</span></div>
  <div class="member-card"><div class="member-photo" role="img" aria-label="Portrait photo of a team member in a vest"></div></div>
  <div class="dots"><i></i><i></i></div>
</section>

<footer class="site-footer">
  <div class="foot-brand"><span>NovaKin</span><span class="brand-dot"></span></div>
  <div class="round-ico" style="left:78px;top:129px">
    <svg width="18" height="22" viewBox="0 0 18 22"><path fill="#fff" d="M9 0a8 8 0 0 1 8 8c0 6-8 14-8 14S1 14 1 8a8 8 0 0 1 8-8z"/><circle cx="9" cy="8" r="3" fill="#35aee2"/></svg>
  </div>
  <div class="foot-addr"><strong>Nova Kin</strong>48 Larch Row Ste B<br>Milford IA, 50200</div>
  <div class="foot-nav"><span class="on">Home</span><em>|</em>About<em>|</em>Vision<em>|</em>Mission<em>|</em>Team<em>|</em>Contact</div>
  <div class="social" style="left:549px;background:var(--fb)"></div>
  <div class="social" style="left:584px;background:var(--red)"></div>
  <div class="social" style="left:619px;background:var(--sky)"></div>
  <div class="round-ico" style="left:890px;top:124px">
    <svg width="18" height="18" viewBox="0 0 24 24"><path fill="#fff" d="M6.6 10.8a15 15 0 0 0 6.6 6.6l2.2-2.2a1 1 0 0 1 1-.25 11.4 11.4 0 0 0 3.6.6 1 1 0 0 1 1 1V20a1 1 0 0 1-1 1A17 17 0 0 1 3 4a1 1 0 0 1 1-1h3.5a1 1 0 0 1 1 1c0 1.25.2 2.45.6 3.6a1 1 0 0 1-.25 1z"/></svg>
  </div>
  <div class="foot-contact" style="top:135px">+1 555 010 4477</div>
  <div class="round-ico" style="left:890px;top:178px">
    <svg width="18" height="14" viewBox="0 0 18 14"><rect width="18" height="14" rx="2" fill="#fff"/><path d="M1 1l8 6 8-6" fill="none" stroke="#35aee2" stroke-width="1.6"/></svg>
  </div>
  <div class="foot-contact" style="top:189px">hello@novakin.com</div>
</footer>

<div class="bottom-bar">
  <span style="left:79px">© <b>NOVA KIN</b> &nbsp;|&nbsp; 2018 All Rights Reserved</span>
  <span style="left:903px">Terms of Use and Privacy Policy</span>
</div>

</body>
</html>
```